Finding Amber Gate Keepers (Book cover)

This project is for a book I am currently writing. It will help pastors and church leaders communicate why serving in the local church is the so important and how to motivate them to serve at high levels.

The title of the book comes from the passage of scripture where Jesus said, "when a solider demands you to carry his gear one mile, go with him two." He wants his followers to willingly do more than is expected. Doing the minimum seldom does much to change hearts of people around us.

This book will deal with these concepts and help leaders train others to follow in this line of thinking - to be Amber Gate Keepers.

Target Market(s)

church leaders, christian book readers

Industry/Entity Type

Church

Font styles to use
Sans Serif

Colors
fece3e

Requirements
Must have
• Catchy color, font layout to attract readers to take a 2nd look inside the book. Lots of empty space on the cover art, gradient color, sharp contrasts. Large Letters
Nice to have
• A central image on the artwork that will communicate the metaphor of going the 2nd mile.
Should not have
• any imagery that is suggestive

```html
<!DOCTYPE html>
<html lang="en">
<head>
<meta charset="utf-8">
<title>Finding Amber Gate Keepers — Book Cover</title>
<link rel="stylesheet" href="https://fonts.googleapis.com/css2?family=Source+Sans+3:wght@400;700;800&display=swap">
<style>
  :root {
    --amber: #fccf3e;
    --paper: #ffffff;
    --ink: #000000;
  }
  html, body {
    margin: 0;
    padding: 0;
    width: 1133px;
    height: 1200px;
    overflow: hidden;
    background: var(--amber);
  }
  .cover {
    position: relative;
    width: 1133px;
    height: 1200px;
    background: var(--amber);
    font-family: "Source Sans 3", Arial, sans-serif;
    color: var(--ink);
  }
  .cover__title {
    margin: 0;
    font-weight: inherit;
    font-size: inherit;
  }
  .cover__rule {
    position: absolute;
    left: 0;
    top: 299px;
    width: 100%;
    height: 1.5px;
    background: var(--paper);
  }
  .cover__author-band {
    position: absolute;
    left: 0;
    top: 457px;
    width: 100%;
    height: 181px;
    background: var(--paper);
  }
  .cover__line {
    position: absolute;
    left: 0;
    width: 100%;
    margin: 0;
    text-align: center;
    line-height: 1;
    white-space: nowrap;
    box-sizing: border-box;
  }
  .title-lead {
    top: 38px;
    font-weight: 700;
    font-size: 60px;
    letter-spacing: 0.3em;
    padding-left: 0.3em;
  }
  .title-word {
    font-weight: 800;
  }
  .title-word--top {
    top: 118px;
    font-size: 140px;
    letter-spacing: 0.14em;
    padding-left: 0.14em;
  }
  .title-word--bottom {
    top: 740px;
    font-size: 170px;
    letter-spacing: 0.2em;
    padding-left: 0.2em;
  }
  .author {
    top: 505px;
    font-weight: 400;
    font-size: 90px;
  }
  .tagline {
    position: absolute;
    top: 960px;
    left: 0;
    width: 100%;
    margin: 0;
    text-align: center;
    font-weight: 400;
    font-size: 60px;
    line-height: 82px;
  }
  .tagline__row {
    display: block;
    white-space: nowrap;
  }
</style>
</head>
<body>
  <main class="cover">
    <h1 class="cover__title">
      <span class="cover__line title-lead">Finding</span>
      <span class="cover__line title-word title-word--top">Amber Gate</span>
      <span class="cover__line title-word title-word--bottom">Keepers</span>
    </h1>
    <div class="cover__rule"></div>
    <div class="cover__author-band"></div>
    <p class="cover__line author">Author Name</p>
    <p class="tagline">
      <span class="tagline__row">when a solider demands you</span>
      <span class="tagline__row">to carry his gear one mile, go</span>
      <span class="tagline__row">with him two</span>
    </p>
  </main>
</body>
</html>
```